Etiketten-Design für eine recycelte Flagge gesucht
Zielgruppe
Wir bieten Länderfahnen z.B. Deutschland Flaggen usw. an. In diesem Fall geht es um recycelte Flagge - das Material wird aus alten Plastikflaschen gewonnen
Aufgabenstellung
Etikett für eine recycelte Flagge
Das Etikett wird für mehrere verschiedene Designs verwendet, daher hier nur als Beispiel die Deutschland Flagge.
Größe: 12x6cm
Druckart: Digitaldruck
Druckdatei: pdf
folgende Infos müssen enthalten sein:
(Beispielhaft an der Deutschland Flagge)
Name: Deutschland Flagge in recycelter Premium Qualität
Artikelnummer: 372
EAN Code: 4251938407561
Material: Polyester recycelt
Größe: 90 x 150 cm
(wenn möglich => Grafische Darstellung der Deutschland Flagge - KEIN FOTO)
Logo: siehe Dateien
Anschrift:
velumor GmbH
Am Hang 8
79346 Talbrunn - Germany
info@velumor.com
URL des Shops: www.quiro-banner.com
Das Etikett wird auf einer braunen Papiertüte angebracht.

```html
<!DOCTYPE html>
<html lang="de">
<head>
<meta charset="utf-8">
<title>Etikett – Deutschland Flagge recycelt</title>
<link rel="stylesheet" href="https://fonts.googleapis.com/css2?family=Roboto:wght@400;700&display=swap">
<style>
  :root {
    --ink: #111111;
    --paper: #ffffff;
    --tone-dark: #2e2e2e;
    --tone-red: #e0393a;
    --tone-gold: #f4e61e;
  }
  * { margin: 0; padding: 0; box-sizing: border-box; }
  html, body { width: 1200px; height: 600px; overflow: hidden; background: var(--paper); }
  .label {
    position: relative;
    width: 1200px;
    height: 600px;
    background: var(--paper);
    border: 5px solid var(--ink);
    font-family: "Roboto", Arial, sans-serif;
    color: var(--ink);
  }
  .label__frame {
    position: absolute;
    left: 14px; top: 12px; right: 14px; bottom: 12px;
    border: 2.5px solid var(--ink);
  }
  .brand {
    position: absolute;
    top: 78px; left: 0; right: 0;
    display: flex; justify-content: center; align-items: center; gap: 10px;
  }
  .brand__dot { width: 14px; height: 14px; border-radius: 50%; background: var(--ink); }
  .brand__name { font-weight: 700; font-size: 26px; letter-spacing: 1px; text-transform: uppercase; }
  .title {
    position: absolute;
    top: 168px; left: 0; right: 0;
    text-align: center;
    font-weight: 700;
    font-size: 35px;
    line-height: 42px;
    text-transform: uppercase;
  }
  .flag-art {
    position: absolute;
    left: 536px; top: 280px;
    width: 136px; height: 100px;
    background: linear-gradient(180deg, var(--tone-dark) 0%, var(--tone-red) 50%, var(--tone-gold) 100%);
  }
  .specs {
    position: absolute;
    top: 399px; left: 0; right: 0;
    text-align: center;
    font-size: 22px;
    line-height: 28px;
  }
  .divider {
    position: absolute;
    top: 481px; left: 329px;
    width: 542px; height: 0;
    border-top: 1.5px solid var(--ink);
  }
  .contact {
    position: absolute;
    top: 500px; left: 0; right: 0;
    text-align: center;
    font-size: 22px;
    line-height: 27px;
  }
</style>
</head>
<body>
  <div class="label">
    <div class="label__frame"></div>

    <div class="brand">
      <span class="brand__dot"></span>
      <span class="brand__name">Quiro Banner</span>
    </div>

    <h1 class="title">Deutschland Flagge<br>in recycelter Premium Qualität</h1>

    <div class="flag-art" role="img" aria-label="Grafik einer wehenden Deutschland Flagge in Schwarz, Rot, Gold"></div>

    <div class="specs">
      <p>Artikelnummer: 372 I EAN Code: 4251938407561</p>
      <p>Material: Polyester recycelt I Größe: 90 x 150 cm</p>
    </div>

    <div class="divider"></div>

    <div class="contact">
      <p>Velumor GmbH I Am Hang 8, 79346 Talbrunn - Germany</p>
      <p>E-mail: info@velumor.com I Tel.: +49 7602 418 273 I www.quiro-banner.com</p>
    </div>
  </div>
</body>
</html>
```